Safety Brochure for Industry Assocations

This is an 8.5 x 11 single sided brochure for our Occupational Health and Safety Data Analytics software. If you need to use stock images we will pay for them.

Please incorporate our logo and some of the images. No need to incorporate them all. We like the idea of the boots being at the bottom of the page but we're open to other ideas.

Please note that we intend to mail this brochure to different industries so it should be generic (i.e. not construction specific).

Target Market(s)

Safety and Industry Organisations for construction, mining, forestry and oil and gas industries.

Industry/Entity Type

Industry

Font styles to use
Sans Serif

Colors

Designer to choose colors to be used in the design.

Requirements
Must have
• We are a software company that produces safety software. Our customers are companies that engage in dangerous work and use our software to improve their worker's safety. The look and feel should convey the fact that:
• -We are Big Data
• -We are Software
• -We service industry
Nice to have
• Please see the Pixfold photo of the boots. We were hoping that the desiger would be able ti modify the image with an overlay of 0's and 1's in a kind of "matrix" fashion to indicate that we are merging traditional labour work with software.
Should not have
• No medical symbols. Note that WE ARE NOT HEALTH CARE.

```html
<!DOCTYPE html>
<html lang="en">
<head>
<meta charset="utf-8">
<title>Leverage the power of Big Data</title>
<link href="https://fonts.googleapis.com/css2?family=Roboto:wght@400;700;900&display=swap" rel="stylesheet">
<style>
  :root {
    --navy: #1b4a72;
    --navy-deep: #173f63;
    --teal: #1f7ea6;
    --chevron-light: #2e7fb0;
    --ink: #1d3c60;
    --green: #5cb531;
    --soft-grey: #eef1f3;
    --white: #ffffff;
    --line: #555a60;
    --black: #111111;
  }
  html, body { margin: 0; padding: 0; overflow: hidden; }
  body { background: var(--white); font-family: "Roboto", sans-serif; }
  .brochure { position: relative; width: 927px; height: 1200px; overflow: hidden; background: var(--white); }
  .artwork { position: absolute; inset: 0; }
  .headline { fill: var(--white); text-anchor: middle; font-family: "Roboto", sans-serif; }
  .headline-lead { font-size: 34px; font-weight: 400; }
  .headline-big { font-size: 54px; font-weight: 900; }
  .node-text { fill: var(--white); font-weight: 700; text-anchor: middle; font-family: "Roboto", sans-serif; }
  .cloud-text { fill: var(--white); font-size: 32px; font-weight: 400; text-anchor: middle; font-family: "Roboto", sans-serif; }
  .brand { position: absolute; left: 626px; top: 38px; display: flex; align-items: center; gap: 10px; }
  .brand-dot { width: 50px; height: 50px; border-radius: 50%; background: var(--green); flex: none; }
  .brand-name { font-size: 27px; font-weight: 700; color: var(--ink); line-height: 1; white-space: nowrap; }
  .pillars { position: absolute; left: 16px; top: 231px; margin: 0; padding: 0; list-style: none; }
  .pillar { display: flex; align-items: center; height: 59px; }
  .pillar-num { width: 52px; height: 52px; border-radius: 50%; background: var(--navy-deep); color: var(--white);
    font-size: 32px; font-weight: 900; display: flex; align-items: center; justify-content: center; flex: none; }
  .pillar-text { margin-left: 14px; color: var(--ink); line-height: 1.2; }
  .pillar-title { font-size: 21px; font-weight: 400; }
  .pillar-sub, .pillar-inline { font-size: 15px; font-weight: 700; }
  .step { position: absolute; color: var(--ink); font-size: 23px; font-weight: 900; line-height: 32px; }
  .step-location { left: 11px; top: 640px; }
  .step-upload { left: 181px; top: 782px; }
  .step-dashboard { left: 11px; top: 918px; }
  .phone { position: absolute; right: 22px; top: 1144px; font-size: 24px; font-weight: 900; color: var(--black); }
</style>
</head>
<body>
<main class="brochure">
  <svg class="artwork" width="927" height="1200" viewBox="0 0 927 1200">
    <defs>
      <linearGradient id="bootTone" x1="0" y1="0" x2="0" y2="1">
        <stop offset="0" stop-color="#1a2a12"/>
        <stop offset="1" stop-color="#0c1408"/>
      </linearGradient>
    </defs>

    <g class="headline-cloud" fill="var(--navy)">
      <rect x="0" y="0" width="570" height="150"/>
      <circle cx="40" cy="150" r="50"/>
      <circle cx="125" cy="168" r="50"/>
      <circle cx="220" cy="172" r="48"/>
      <circle cx="315" cy="168" r="48"/>
      <circle cx="410" cy="158" r="50"/>
      <circle cx="505" cy="135" r="52"/>
      <circle cx="555" cy="70" r="55"/>
    </g>
    <text class="headline headline-lead" x="275" y="58">Leverage the power of</text>
    <text class="headline headline-big" x="275" y="125">Big Data!</text>

    <g stroke="var(--line)" stroke-width="1.5" fill="none">
      <line x1="598" y1="285" x2="478" y2="440"/>
      <line x1="640" y1="288" x2="640" y2="440"/>
      <line x1="680" y1="285" x2="818" y2="440"/>
      <line x1="472" y1="730" x2="590" y2="845"/>
      <line x1="640" y1="730" x2="640" y2="815"/>
      <line x1="820" y1="730" x2="695" y2="845"/>
    </g>

    <g class="data-cloud" fill="var(--navy)">
      <ellipse cx="640" cy="245" rx="130" ry="44"/>
      <circle cx="585" cy="215" r="42"/>
      <circle cx="648" cy="192" r="44"/>
      <circle cx="712" cy="215" r="40"/>
      <circle cx="540" cy="250" r="32"/>
      <circle cx="748" cy="252" r="32"/>
    </g>
    <text class="cloud-text" x="640" y="212">EHS</text>
    <text class="cloud-text" x="640" y="252">DATA</text>

    <g fill="var(--teal)">
      <circle cx="472" cy="480" r="46"/>
      <circle cx="642" cy="484" r="46"/>
      <circle cx="825" cy="480" r="46"/>
    </g>
    <text class="node-text" font-size="17" x="472" y="486">Training</text>
    <text class="node-text" font-size="17" x="642" y="478">Bench-</text>
    <text class="node-text" font-size="17" x="642" y="499">marking</text>
    <text class="node-text" font-size="17" x="825" y="474">Trend</text>
    <text class="node-text" font-size="17" x="825" y="495">Analysis</text>

    <g fill="none">
      <g id="chevron-stack">
        <polyline points="403,512 472,550 541,512" stroke="var(--navy)" stroke-width="14"/>
        <polyline points="403,530 472,568 541,530" stroke="var(--chevron-light)" stroke-width="10"/>
        <polyline points="403,546 472,584 541,546" stroke="var(--navy)" stroke-width="12"/>
      </g>
      <use href="#chevron-stack" x="170"/>
      <use href="#chevron-stack" x="353"/>
    </g>

    <g fill="var(--navy-deep)">
      <rect x="401" y="594" width="142" height="56" rx="28"/>
      <rect x="571" y="594" width="142" height="56" rx="28"/>
      <rect x="754" y="594" width="142" height="56" rx="28"/>
      <rect x="401" y="673" width="142" height="60" rx="30"/>
      <rect x="571" y="673" width="142" height="60" rx="30"/>
      <rect x="754" y="673" width="142" height="60" rx="30"/>
    </g>
    <text class="node-text" font-size="14"><tspan x="472" y="617">Analyze</tspan><tspan x="472" y="636">Need of Industry</tspan></text>
    <text class="node-text" font-size="14"><tspan x="642" y="617">Engage</tspan><tspan x="642" y="636">With Members</tspan></text>
    <text class="node-text" font-size="14"><tspan x="825" y="617">Monitor</tspan><tspan x="825" y="636">Industry Trends</tspan></text>
    <text class="node-text" font-size="12"><tspan x="472" y="698">Deliver</tspan><tspan x="472" y="715">Proactive Training</tspan></text>
    <text class="node-text" font-size="10"><tspan x="642" y="692">Promote</tspan><tspan x="642" y="705">Collaborative</tspan><tspan x="642" y="718">Advancement of Safety</tspan></text>
    <text class="node-text" font-size="12"><tspan x="825" y="690">Implement</tspan><tspan x="825" y="704">Corrective</tspan><tspan x="825" y="718">Initiatives</tspan></text>

    <circle cx="640" cy="887" r="74" fill="var(--teal)"/>
    <text class="node-text" font-size="24"><tspan x="640" y="882">Improve</tspan><tspan x="640" y="912">Safety</tspan></text>

    <circle cx="232" cy="678" r="56" fill="var(--soft-grey)"/>
    <circle cx="232" cy="678" r="40" fill="var(--green)" role="img" aria-label="Globe with location pin icon"/>
    <circle cx="90" cy="819" r="56" fill="var(--soft-grey)"/>
    <rect x="58" y="788" width="64" height="60" rx="6" fill="var(--green)" role="img" aria-label="Upload window with gears icon"/>
    <circle cx="232" cy="950" r="56" fill="var(--soft-grey)"/>
    <rect x="194" y="924" width="76" height="52" rx="4" fill="var(--green)" role="img" aria-label="Desktop and mobile dashboard icon"/>

    <path d="M338 992 H620 V1172 H252 V1092 H338 Z" fill="url(#bootTone)" stroke="var(--green)" stroke-width="3" stroke-linejoin="round"
          role="img" aria-label="Pair of work boots overlaid with green binary digits"/>
  </svg>

  <div class="brand">
    <span class="brand-dot"></span>
    <span class="brand-name">Vantix Analytics</span>
  </div>

  <ol class="pillars">
    <li class="pillar"><span class="pillar-num">1</span><span class="pillar-text"><span class="pillar-title">LEAD</span><br><span class="pillar-sub">The next wave of injury reduction</span></span></li>
    <li class="pillar"><span class="pillar-num">2</span><span class="pillar-text"><span class="pillar-title">ENGAGE</span><br><span class="pillar-sub">With Members by Collaboration and Benchmarking</span></span></li>
    <li class="pillar"><span class="pillar-num">3</span><span class="pillar-text"><span class="pillar-title">PROMOTE</span> <span class="pillar-inline">Standardization</span></span></li>
    <li class="pillar"><span class="pillar-num">4</span><span class="pillar-text"><span class="pillar-title">ANALYZE</span><br><span class="pillar-sub">Accurate, Timely &amp;<br>Complete Leading Indicators</span></span></li>
    <li class="pillar"><span class="pillar-num">5</span><span class="pillar-text"><span class="pillar-title">TRAIN</span><br><span class="pillar-sub">Industry more Proactively</span></span></li>
  </ol>

  <div class="step step-location">Set up<br>Your<br>Location</div>
  <div class="step step-upload">Upload<br>Your<br>Data</div>
  <div class="step step-dashboard">Start<br>Using Your<br>Dashboard</div>

  <div class="phone">1-888-555-0142</div>
</main>
</body>
</html>
```